Book cover

I am working with my publisher to publish my book They came up with a book cover but I don't like it. I want to see different designs. The book Title is Shiftcraftery the subtitle How to Steer Upheaval with Focus, Poise & Resolve by Marilyn T. Hargreave
I want to use my Brand Colors including the blue. I am uploading the covers of my other book. This is a professional leadership book. The publisher will make the cover when providing them a new design. the Shiftcraftery one is one I played with on Canva. I would like more color and to incorporate the blue. I want a spot at the top where I can write a quote. Shiftcraftery is one word in the text so should be the same on the cover. I want the cover to show energy movement and am open to an image too. I am attaching logos for the feel of the brand and brand rgb codes.

```html
<!DOCTYPE html>
<html lang="en">
<head>
<meta charset="utf-8">
<title>Shiftcraftery — Book Cover</title>
<link rel="stylesheet" href="https://fonts.googleapis.com/css2?family=Anton&family=Montserrat:ital,wght@0,500;1,500&display=swap">
<style>
  :root {
    --brand-blue: #0033a0;
    --brand-sky: #2f80ed;
    --accent-red: #e60000;
    --accent-gold: #f5a623;
    --ink: #111111;
    --paper: #ffffff;
  }
  html, body {
    margin: 0;
    padding: 0;
    width: 1200px;
    height: 1200px;
    overflow: hidden;
    background: var(--paper);
  }
  .canvas {
    position: relative;
    width: 1200px;
    height: 1200px;
  }
  .book-cover {
    position: absolute;
    left: 229px;
    top: 46px;
    width: 735px;
    height: 1102px;
    overflow: hidden;
    box-shadow: 0 0 0 1px rgba(160,170,200,0.35);
  }
  .book-cover svg {
    display: block;
    width: 100%;
    height: 100%;
  }
  .quote-band { fill: var(--brand-blue); }
  .quote-rule { fill: var(--accent-red); }
  .quote-text {
    font-family: "Montserrat", sans-serif;
    font-style: italic;
    font-weight: 500;
    fill: var(--paper);
  }
  .quote-source {
    font-family: "Montserrat", sans-serif;
    font-weight: 500;
    fill: var(--paper);
    opacity: 0.85;
    letter-spacing: 1px;
  }
  .cover-title {
    font-family: "Anton", "Oswald", sans-serif;
    fill: var(--brand-blue);
  }
  .cover-subtitle {
    font-family: "Montserrat", sans-serif;
    font-weight: 500;
    fill: var(--ink);
  }
  .author-band { fill: var(--brand-blue); }
  .author-name {
    font-family: "Montserrat", sans-serif;
    font-weight: 500;
    fill: var(--paper);
    letter-spacing: 1px;
  }
  .swoosh { fill: none; stroke-linecap: round; }
  .swoosh-blue { stroke: var(--brand-blue); }
  .swoosh-sky { stroke: var(--brand-sky); }
  .swoosh-red { stroke: var(--accent-red); }
  .swoosh-gold { stroke: var(--accent-gold); }
  .streak { stroke-linecap: round; }
</style>
</head>
<body>
<div class="canvas">
  <div class="book-cover">
    <svg viewBox="0 0 900 1350" xmlns="http://www.w3.org/2000/svg">
      <defs>
        <radialGradient id="coverGlow" cx="450" cy="660" r="760" gradientUnits="userSpaceOnUse">
          <stop offset="0" stop-color="#ffffff"/>
          <stop offset="0.45" stop-color="#f1f3f9"/>
          <stop offset="1" stop-color="#d3d9ea"/>
        </radialGradient>
      </defs>

      <rect class="cover-background" x="0" y="0" width="900" height="1350" fill="url(#coverGlow)"/>

      <g class="quote-area">
        <rect class="quote-band" x="0" y="0" width="900" height="190"/>
        <rect class="quote-rule" x="0" y="190" width="900" height="8"/>
        <text class="quote-text" font-size="30" text-anchor="middle">
          <tspan x="450" y="78">“Place a short endorsement quote</tspan>
          <tspan x="450" y="118">here to welcome new readers.”</tspan>
        </text>
        <text class="quote-source" x="450" y="158" font-size="20" text-anchor="middle">— ENDORSER NAME, TITLE</text>
      </g>

      <g class="energy-upper">
        <path class="swoosh swoosh-sky" d="M -60 520 C 250 420, 560 470, 960 250" stroke-width="44" opacity="0.22"/>
        <path class="swoosh swoosh-blue" d="M -60 500 C 260 400, 560 440, 960 230" stroke-width="16"/>
        <path class="swoosh swoosh-red" d="M -60 455 C 270 360, 570 400, 960 200" stroke-width="7"/>
        <path class="swoosh swoosh-gold" d="M -60 540 C 240 450, 560 490, 960 285" stroke-width="5"/>
        <line class="streak" x1="640" y1="300" x2="760" y2="262" stroke="#2f80ed" stroke-width="4" opacity="0.6"/>
        <line class="streak" x1="120" y1="390" x2="220" y2="362" stroke="#e60000" stroke-width="4" opacity="0.7"/>
      </g>

      <g class="energy-lower">
        <path class="swoosh swoosh-sky" d="M -60 1200 C 300 1080, 600 1130, 960 900" stroke-width="50" opacity="0.22"/>
        <path class="swoosh swoosh-blue" d="M -60 1175 C 300 1055, 600 1100, 960 875" stroke-width="18"/>
        <path class="swoosh swoosh-red" d="M -60 1130 C 310 1010, 610 1050, 960 840" stroke-width="8"/>
        <path class="swoosh swoosh-gold" d="M -60 1215 C 290 1100, 600 1150, 960 930" stroke-width="5"/>
        <line class="streak" x1="660" y1="990" x2="780" y2="950" stroke="#f5a623" stroke-width="4" opacity="0.8"/>
        <line class="streak" x1="90" y1="1080" x2="200" y2="1050" stroke="#2f80ed" stroke-width="4" opacity="0.6"/>
      </g>

      <text class="cover-title" x="74" y="690" font-size="170" textLength="752" lengthAdjust="spacingAndGlyphs">Shiftcraftery</text>

      <text class="cover-subtitle" font-size="33" text-anchor="middle">
        <tspan x="450" y="780">How to Steer Upheaval with</tspan>
        <tspan x="450" y="822">Focus, Poise &amp; Resolve</tspan>
      </text>

      <rect class="author-band" x="0" y="1231" width="900" height="119"/>
      <text class="author-name" x="450" y="1305" font-size="52" text-anchor="middle">Marilyn T. Hargreave</text>
    </svg>
  </div>
</div>
</body>
</html>
```